Postcard Design

We need a postcard designed for our company Clastor-Ox. Clastor-ox specializes in providing a tailored document destruction service that allows businesses to comply with legislation and ensure that the client, employee and confidential business information is kept secure at all times. We would like to see a postcard with greys, blues, blacks, and whites in it. I have attached a few logos for your reference. I would like the front of the postcard to be a picture design only with our company logo info. The back should have a message that says:

Dear Valued Customer,
We are sending you this letter because you currently utilize our On-site paper destruction service. We want to make you aware of our Plant-Based paper destruction service and the benefits to you and to the environment. Currently, 60% of our customers receive, and are highly satisfied with our Plant-Based Service.

Definitions:
On-site Service – Customer’s material is destroyed at the Customer’s location
Plant-Based Service – Customer’s material is destroyed at a Clastor-ox Secured Facility

What Would Not Change:

Security:
- All trucks are equipped with GPS tracking devices
- Our facility is monitored by CCTV 24 hours a day 7 days a week
- Our box trucks are equipped with secure alarm systems
- Annual Background Checks and Drug Screens are ran on all employees

Plant-Based Service Benefits:
- Less Noise at your Location
- Less Time in your Parking Lot
- Reduced Fuel Consumption
- Environmentally Friendly
- Flexibility
- Quicker turn-around times on all Service Requests (i.e., Purges / Earlier Pick-Ups)

We will begin changing your service from On-site to Plant Based starting August 1st. The process will take an additional 60 days to fully implement so you may not see a change right away. Our On-site capabilities are NOT going away. If you wish to remain an On-site customer all you have to do is call or email me your request. I am also available should you have any questions. My contact information is below.
We appreciate your consideration in regards to this matter and, as always, thank you for your business.

Martin L. Pruett
General Manager
Martin.Pruett@clastorox-mail.com
472.618.5037

is there enough room to get this on the back of the card?

Industry/Entity Type

It Company

```html
<!DOCTYPE html>
<html lang="en">
<head>
<meta charset="utf-8">
<title>Clastor-Ox Postcard – Back</title>
<link href="https://fonts.googleapis.com/css2?family=Delius&family=Oswald:wght@500;600&family=PT+Sans+Narrow:wght@400;700&family=Source+Sans+3:ital,wght@0,300;0,400;0,600;0,700;1,400&display=swap" rel="stylesheet">
<style>
  :root {
    --navy: #173b86;
    --blue: #2f6cc2;
    --blue-deep: #1c4597;
    --band: #2b2b2d;
    --ink: #1b1b1b;
    --icon: #5a6f8c;
    --white: #ffffff;
    --mist: #b9c6dc;
    --rule: #dcdcdc;
    --stamp: #cfcfcf;
  }
  * { box-sizing: border-box; margin: 0; padding: 0; }
  html, body { width: 1200px; height: 930px; overflow: hidden; background: var(--white); }
  .postcard { position: relative; width: 1200px; height: 930px; background: var(--white); }

  .message-panel {
    position: absolute; left: 0; top: 0; width: 578px; height: 708px; overflow: hidden;
    background: radial-gradient(ellipse 90% 70% at 60% 55%, var(--blue) 0%, var(--blue-deep) 70%, var(--navy) 100%);
    color: var(--white);
  }
  .greeting {
    position: absolute; left: 30px; top: 30px;
    font: 22px/1 "Delius", cursive;
  }
  .intro {
    position: absolute; left: 30px; top: 58px; width: 545px;
    font: 300 18.5px/21px "Source Sans 3", sans-serif;
  }
  .definitions {
    position: absolute; left: 0; top: 170px; width: 578px; height: 74px;
    background: var(--band); text-align: center;
  }
  .definitions h2 {
    font: 600 27px/1 "Oswald", sans-serif; letter-spacing: .5px; padding-top: 4px;
  }
  .definitions p { font: 400 17px/21px "PT Sans Narrow", sans-serif; color: #e6e6e6; }
  .definitions h2 + p { margin-top: 4px; }

  .security-row {
    position: absolute; left: 0; top: 246px; width: 578px; height: 116px;
    display: flex; gap: 4px; background: var(--blue-deep); padding-bottom: 2px;
  }
  .security-item {
    flex: 1; background: var(--white); text-align: center; padding-top: 5px; white-space: nowrap;
    font: 700 16px/20px "PT Sans Narrow", sans-serif; color: var(--ink); overflow: hidden;
  }
  .security-item.tight { font-size: 14.5px; letter-spacing: -.5px; }
  .security-item svg { display: block; margin: 0 auto 8px; height: 34px; }

  .benefits-title {
    position: absolute; left: 22px; top: 377px;
    font: 600 25px/1 "Oswald", sans-serif; letter-spacing: .3px;
    padding: 2px 6px 3px 8px; border-left: 3px solid var(--white); border-bottom: 3px solid var(--white);
  }
  .benefits {
    position: absolute; top: 418px; list-style: none; white-space: nowrap;
    font: 400 19px/27px "PT Sans Narrow", sans-serif;
  }
  .benefits.col-a { left: 26px; }
  .benefits.col-b { left: 240px; }
  .benefits .long { letter-spacing: -.5px; }
  .benefits .note { display: block; font-size: 15px; line-height: 15px; padding-left: 10px; letter-spacing: 0; }

  .letter-close {
    position: absolute; left: 32px; top: 530px; width: 536px;
  }
  .change-notice {
    font: 600 17px/21px "Source Sans 3", sans-serif; letter-spacing: -.3px;
  }
  .closing {
    margin: 8px 0 0 48px; width: 470px;
    font: 700 17.5px/19px "Source Sans 3", sans-serif; color: var(--mist); letter-spacing: -.2px;
  }

  .signature {
    position: absolute; left: 0; top: 710px; width: 578px; text-align: center; color: var(--ink);
  }
  .signature .name { font: 400 22px/27px "Source Sans 3", sans-serif; }
  .signature .role { font-style: italic; font-size: 19px; }
  .signature .contact {
    font: 700 20px/24px "Source Sans 3", sans-serif; display: flex; justify-content: center; align-items: center; gap: 5px;
  }
  .contact-dot {
    display: inline-flex; width: 17px; height: 17px; border-radius: 50%; background: var(--blue);
    color: var(--white); font-size: 11px; align-items: center; justify-content: center;
  }
  .contact-dot.phone { margin-left: 6px; }

  .stamp-box {
    position: absolute; left: 908px; top: 27px; width: 266px; height: 269px;
    border: 2px solid var(--stamp);
  }
  .address-line {
    position: absolute; left: 645px; width: 496px; height: 0; border-top: 3px solid var(--rule);
  }
</style>
</head>
<body>
<main class="postcard">
  <section class="message-panel">
    <p class="greeting">Dear Valued Customer,</p>
    <p class="intro">We are sending you this letter because you currently utilize our On-site paper destruction service. We want to make you aware of our Plant-Based paper destruction service and the benefits to you and to the environment. Currently, 60% of our customers receive, and are highly satisfied with our Plant-Based Service.</p>

    <div class="definitions">
      <h2>DEFINITIONS:</h2>
      <p>On-site Service – Customer’s material is destroyed at the Customer’s location</p>
      <p>Plant-Based Service – Customer’s material is destroyed at a Clastor-ox Secured Facility</p>
    </div>

    <div class="security-row">
      <div class="security-item">
        <svg viewBox="0 0 50 32" width="54" aria-hidden="true"><g fill="var(--icon)"><rect x="2" y="4" width="28" height="19" rx="2"/><path d="M32 10h9l6 7v6H32z"/><circle cx="11" cy="26" r="4.5"/><circle cx="40" cy="26" r="4.5"/></g><g fill="#fff"><circle cx="11" cy="26" r="1.8"/><circle cx="40" cy="26" r="1.8"/></g></svg>
        All trucks are<br>equipped with GPS<br>tracking devices
      </div>
      <div class="security-item">
        <svg viewBox="0 0 50 34" width="50" aria-hidden="true"><g fill="var(--icon)"><path d="M4 10l32-8 3 10-32 8z"/><rect x="36" y="1" width="4" height="30"/><rect x="30" y="15" width="8" height="4"/><path d="M10 19l5-1 2 8-5 1z"/></g></svg>
        Our facility is<br>monitored by CCTV<br>24/7 days a week
      </div>
      <div class="security-item">
        <svg viewBox="0 0 50 34" width="50" aria-hidden="true"><g fill="none" stroke="var(--icon)" stroke-width="3.5" stroke-linecap="round"><path d="M12 5q-8 12 0 24"/><path d="M38 5q8 12 0 24"/><path d="M18 10q-4 7 0 14"/><path d="M32 10q4 7 0 14"/></g><circle cx="25" cy="17" r="4.5" fill="var(--icon)"/></svg>
        Our box trucks are<br>equipped with secure<br>alarm systems
      </div>
      <div class="security-item tight">
        <svg viewBox="0 0 50 34" width="50" aria-hidden="true"><g fill="var(--icon)"><circle cx="13" cy="11" r="6"/><circle cx="37" cy="11" r="6"/><path d="M2 32q0-13 11-13t11 13z"/><path d="M26 32q0-13 11-13t11 13z"/><circle cx="25" cy="9" r="7"/><path d="M12 34q0-16 13-16t13 16z"/></g></svg>
        Annual Background<br>Checks and Drug Screens<br>are ran on all employees
      </div>
    </div>

    <h2 class="benefits-title">PLANT-BASED SERVICE BENEFITS:</h2>
    <ul class="benefits col-a">
      <li>- Less Noise at your Location</li>
      <li>- Less Time in your Parking Lot</li>
      <li>- Reduced Fuel Consumption</li>
    </ul>
    <ul class="benefits col-b">
      <li>- Environmentally Friendly</li>
      <li>- Flexibility</li>
      <li class="long">- Quicker turn-around times on all&nbsp; Service Requests<span class="note">(i.e., Purges / Earlier Pick-Ups)</span></li>
    </ul>

    <div class="letter-close">
      <p class="change-notice">We will begin changing your service from On-site to Plant Based starting August 1st. The process will take an additional 60 days to fully implement so you may not see a change right away. Our On-site capabilities are NOT going away. If you wish to remain an On-site customer all you have to do is call or email me your request. I am also available should you have any questions. My contact information is below.</p>
      <p class="closing">We appreciate your consideration in regards to this matter and, as always, thank you for your business.</p>
    </div>
  </section>

  <footer class="signature">
    <p class="name">Martin L. Pruett <span class="role">General Manager</span></p>
    <p class="contact"><span class="contact-dot">@</span>Martin.Pruett@clastorox-mail.com<span class="contact-dot phone">&#9990;</span>472.618.5037</p>
  </footer>

  <div class="stamp-box"></div>
  <div class="address-line" style="top:419px"></div>
  <div class="address-line" style="top:504px"></div>
  <div class="address-line" style="top:585px"></div>
  <div class="address-line" style="top:667px"></div>
</main>
</body>
</html>
```